buseisness card

design a card that similar to my web site
BRIXENTAPLORLLC .COM

Contact Information for Business Card

NAME PHONE # WEBSITE EMAIL AND DISCTIPTION OF WHAT WE DO

Colors
0054AA
0677BA
7BADD7
CADEEF
E8F1F8

Requirements
Must have
• lOGO AND DETAILS
Nice to have
• I LIKE THE WATER LIKE ON MY WEB SITE

```html
<!DOCTYPE html>
<html lang="en">
<head>
<meta charset="utf-8">
<title>Brixentaplor Business Card</title>
<link href="https://fonts.googleapis.com/css2?family=Montserrat:wght@400;500;700&display=swap" rel="stylesheet">
<style>
  :root {
    --bg: #e8e8ea;
    --navy: #143a54;
    --blue: #1f80b4;
    --white: #ffffff;
    --water-deep: #143a54;
    --water-mid: #2a5f86;
    --water-light: #5f8fb8;
  }
  * { box-sizing: border-box; margin: 0; padding: 0; }
  html, body { width: 1200px; height: 1000px; overflow: hidden; }
  body {
    background: var(--bg);
    font-family: "Montserrat", sans-serif;
    position: relative;
  }
  .card {
    position: absolute;
    left: 303px;
    width: 594px;
    height: 340px;
    border-radius: 22px;
    overflow: hidden;
  }
  .card--front { top: 124px; background: var(--white); }
  .card--back { top: 537px; background: var(--water-deep); }

  .front__brand-panel {
    position: absolute; left: 0; top: 0;
    width: 280px; height: 100%;
    background: var(--navy);
    display: flex; flex-direction: column; align-items: center;
    padding-top: 128px;
  }
  .brand-dot {
    width: 40px; height: 40px; border-radius: 50%;
    background: var(--blue);
    margin-bottom: 16px;
  }
  .brand-name {
    font-weight: 700; font-size: 19px; letter-spacing: 0.2px;
    color: var(--blue);
  }

  .front__details {
    position: absolute; left: 318px; top: 82px;
    color: var(--blue);
  }
  .details__company { font-weight: 700; font-size: 23px; line-height: 28px; }
  .details__role { font-weight: 500; font-size: 16px; line-height: 22px; margin-bottom: 12px; }
  .contact-list { list-style: none; }
  .contact-item {
    display: flex; align-items: flex-start;
    font-size: 15.5px; line-height: 20px;
    margin-bottom: 11px;
  }
  .contact-item svg { width: 13px; height: 13px; margin: 3px 11px 0 0; flex: none; fill: var(--blue); }

  .back__water {
    position: absolute; inset: 0;
    background:
      radial-gradient(ellipse 55% 40% at 55% 50%, var(--water-light) 0%, rgba(95,143,184,0.35) 45%, transparent 75%),
      radial-gradient(ellipse 40% 30% at 20% 30%, rgba(42,95,134,0.8), transparent 70%),
      radial-gradient(ellipse 40% 30% at 85% 45%, rgba(42,95,134,0.8), transparent 70%),
      var(--water-deep);
  }
  .back__brand {
    position: absolute; left: 0; right: 0; top: 206px;
    text-align: center;
    font-weight: 700; font-size: 25px;
    color: var(--white);
  }
</style>
</head>
<body>

<section class="card card--front">
  <div class="front__brand-panel">
    <div class="brand-dot"></div>
    <div class="brand-name">BRIXENTAPLOR</div>
  </div>
  <div class="front__details">
    <h1 class="details__company">BRIXENTAPLOR</h1>
    <p class="details__role">CEO</p>
    <ul class="contact-list">
      <li class="contact-item">
        <svg viewBox="0 0 24 24"><path d="M6.6 10.8a15.1 15.1 0 0 0 6.6 6.6l2.2-2.2c.3-.3.7-.4 1-.2 1.1.4 2.3.6 3.6.6.6 0 1 .4 1 1V20c0 .6-.4 1-1 1A17 17 0 0 1 3 4c0-.6.4-1 1-1h3.5c.6 0 1 .4 1 1 0 1.3.2 2.5.6 3.6.1.3 0 .7-.2 1z"/></svg>
        <span>+740 555 0148</span>
      </li>
      <li class="contact-item">
        <svg viewBox="0 0 24 24"><path d="M2 5h20v14H2z M4 7v.5l8 5 8-5V7l-8 5z" fill-rule="evenodd"/></svg>
        <span>ps@bx131.com</span>
      </li>
      <li class="contact-item">
        <svg viewBox="0 0 24 24"><path d="M12 2a10 10 0 1 0 0 20 10 10 0 0 0 0-20zm6.9 6h-2.9a15 15 0 0 0-1.4-3.6A8 8 0 0 1 18.9 8zM12 4c.8 1.2 1.5 2.5 1.9 4h-3.8c.4-1.5 1.1-2.8 1.9-4zM4.3 14a8 8 0 0 1 0-4h3.4a16 16 0 0 0 0 4zm.8 2h2.9c.3 1.3.8 2.5 1.4 3.6A8 8 0 0 1 5.1 16zM8 8H5.1a8 8 0 0 1 4.3-3.6C8.8 5.5 8.3 6.7 8 8zm4 12c-.8-1.2-1.5-2.5-1.9-4h3.8c-.4 1.5-1.1 2.8-1.9 4zm2.3-6H9.7a14 14 0 0 1 0-4h4.6a14 14 0 0 1 0 4zm.3 5.6c.6-1.1 1.1-2.3 1.4-3.6h2.9a8 8 0 0 1-4.3 3.6zm1.7-5.6a16 16 0 0 0 0-4h3.4a8 8 0 0 1 0 4z"/></svg>
        <span>brixentaplorllc.com</span>
      </li>
      <li class="contact-item">
        <svg viewBox="0 0 24 24"><path d="M12 2a7 7 0 0 0-7 7c0 5.2 7 13 7 13s7-7.8 7-13a7 7 0 0 0-7-7zm0 9.5a2.5 2.5 0 1 1 0-5 2.5 2.5 0 0 1 0 5z"/></svg>
        <span>4180 Harbor Crest<br>Lane<br>Columbus, OH 43215</span>
      </li>
    </ul>
  </div>
</section>

<section class="card card--back">
  <div class="back__water" role="img" aria-label="Blue water splash photograph across the card background"></div>
  <div class="back__brand">BRIXENTAPLOR</div>
</section>

</body>
</html>
```